Yoga Magazine needs 6x9 advertising flyer / postcard

I need a flyer (postcard) for my yoga magazine to hand out to businesses. The front side will serve as a WHO WE ARE, THIS IS WHAT WE DO, ETC....the back side will be ADVERTISING INFORMATION including advertising rates.

please see MS Word doc attached to this brief.

Please bleed artwork on to 6.25" x 9.25" (1/8' extra on all sides)

Target Market(s)

WOMEN ages 20-60 who practice yoga.....and some men, but mostly women.

Industry/Entity Type

Advertising

Font styles to use
Serif

Requirements
Must have
• Please find some stock photos of some nice looking, athletic people doing yoga..
Nice to have
• light and bright colors!
Should not have
• no cartoon figures

```html
<!DOCTYPE html>
<html lang="en">
<head>
<meta charset="utf-8">
<title>Advertising Information</title>
<link href="https://fonts.googleapis.com/css2?family=Jost:wght@300;400;500;600&display=swap" rel="stylesheet">
<style>
  :root {
    --pink: #e0559f;
    --pink-soft: #e477b4;
    --pink-box: rgba(217, 64, 150, 0.9);
    --blue: #3a86d1;
    --blue-box: rgba(45, 120, 200, 0.95);
    --ink: #1d1d1d;
    --white: #ffffff;
    --mat: #5fc0c4;
  }
  * { margin: 0; padding: 0; box-sizing: border-box; }
  html, body { width: 1200px; height: 900px; overflow: hidden; background: var(--white); }
  body { font-family: "Jost", sans-serif; color: var(--ink); }
  .sheet { position: relative; width: 1200px; height: 900px; overflow: hidden; background: var(--white); }

  .headline { position: absolute; top: 28px; left: 0; width: 100%; text-align: center; }
  .headline h1 { font-size: 50px; font-weight: 600; color: var(--pink); letter-spacing: 0.5px; line-height: 1; }
  .headline p { font-size: 22px; font-weight: 300; color: var(--pink-soft); margin-top: 4px; }

  .rate-col { position: absolute; top: 126px; height: 208px; background: var(--blue); color: var(--white); }
  .rate-col h2 { font-size: 22px; font-weight: 500; margin-top: 12px; white-space: nowrap; }
  .rate-col ul { list-style: none; margin-top: 26px; font-size: 14px; font-weight: 300; line-height: 17px; }
  .rate-col.labels { left: 84px; width: 368px; padding-left: 30px; }
  .rate-col.price { width: 160px; text-align: right; padding-right: 14px; }
  .rate-col.price h2 { text-align: right; }
  .c2 { left: 458px; } .c3 { left: 624px; } .c4 { left: 790px; } .c5 { left: 956px; }

  .photo { position: absolute; left: 480px; top: 370px; width: 720px; height: 530px;
    background: linear-gradient(180deg, #ffffff 0%, #f1f2f4 55%, #dcdfe3 80%, var(--mat) 86%, #4aa9ae 100%); }

  .surcharge { position: absolute; left: 110px; top: 362px; font-size: 14px; font-weight: 400; }
  .surcharge strong { font-size: 21px; font-weight: 500; }

  .section { position: absolute; left: 113px; }
  .section h3 { font-size: 22px; font-weight: 500; line-height: 28px; }
  .section ul { list-style: disc; padding-left: 22px; font-size: 14px; font-weight: 400; line-height: 17px; }
  .directories { top: 404px; width: 420px; }
  .events { top: 528px; }

  .specs { position: absolute; left: 84px; top: 590px; width: 426px; height: 292px; background: var(--blue-box);
    color: var(--white); padding: 24px 30px 0 30px; }
  .specs h3 { font-size: 22px; font-weight: 500; margin-bottom: 22px; }
  .specs ul { list-style: disc; padding-left: 20px; font-size: 14px; font-weight: 300; line-height: 17px; }

  .contact { position: absolute; left: 523px; top: 670px; width: 274px; height: 190px; background: var(--pink-box);
    color: var(--white); text-align: center; padding-top: 40px; font-size: 12px; line-height: 17px; font-weight: 400; }
  .contact h4 { font-size: 15px; font-weight: 500; }
</style>
</head>
<body>
<main class="sheet">
  <header class="headline">
    <h1>ADVERTISING INFORMATION</h1>
    <p>(All rates listed are per issue)</p>
  </header>

  <section class="rate-col labels">
    <h2>All rates listed are per issue.</h2>
    <ul>
      <li>Business Card (3.5″w x 2″h)</li>
      <li>1/4 Page (3.8″w x 5″h)</li>
      <li>1/2 Page Horizontal (5″w &nbsp;x 7.75″h)</li>
      <li>1/2 Page Vertical (3.8″w &nbsp;x 10.25″h)</li>
      <li>Full Page (8.5″w x 11″h)</li>
      <li>Page 3 (8.5″w x 11″h)</li>
      <li>Inside Cover (8.5″w x 11″h)</li>
      <li>Back Cover (8.5″w x 11″h)</li>
    </ul>
  </section>
  <section class="rate-col price c2">
    <h2>ONE ISSUE</h2>
    <ul><li>$110</li><li>$225</li><li>$450</li><li>$450</li><li>$800</li><li>$1,500</li><li>$1,225</li><li>$2,250</li></ul>
  </section>
  <section class="rate-col price c3">
    <h2>TWO ISSUES</h2>
    <ul><li>$100</li><li>$210</li><li>$420</li><li>$420</li><li>$750</li><li>$1,425</li><li>$1,150</li><li>$2,200</li></ul>
  </section>
  <section class="rate-col price c4">
    <h2>THREE ISSUES</h2>
    <ul><li>$90</li><li>$195</li><li>$390</li><li>$390</li><li>$725</li><li>$1,350</li><li>$1,075</li><li>$2,150</li></ul>
  </section>
  <section class="rate-col price c5">
    <h2>FOUR ISSUES</h2>
    <ul><li>$75</li><li>$180</li><li>$360</li><li>$360</li><li>$700</li><li>$1,275</li><li>$1,000</li><li>$2,100</li></ul>
  </section>

  <div class="photo" role="img" aria-label="Photo of a woman in blue activewear balancing in crow pose on a teal yoga mat"></div>

  <p class="surcharge"><strong>Color Surcharge:</strong> Full Page add $100; Half Page add $85; ¼ page add $65; Business Card add $35</p>

  <section class="section directories">
    <h3>Directories: &nbsp;Holistic, Restaurant, Green Business and Yoga Related</h3>
    <ul>
      <li>65 Spaces per line, 1 line, FOUR ISSUES for $80</li>
      <li>65 Spaces per line, 2 lines, FOUR ISSUES for $150</li>
      <li>65 Spaces per line, 3 lines, FOUR ISSUES for $225</li>
    </ul>
  </section>

  <section class="section events">
    <h3>Event Listings:</h3>
    <ul><li>50 words for $15 (50 word maximum)</li></ul>
  </section>

  <section class="specs">
    <h3>Ad Specs:</h3>
    <ul>
      <li>Final trim size: 8.5″x11″.</li>
      <li>Please keep text 0.125″ away from edges</li>
      <li>Full-page ad size: 8.25″x10.5″ for non-bleeds; 8.625″x11.25″ for bleeds.</li>
      <li>Please inquire about specs for other print and digital edition positions</li>
      <li>Binding: Saddle stitch</li>
      <li>Stock and inks: Artwork colors should be CMYK; artwork with PMS colors, metallic colors and spot varnish will not be accepted</li>
      <li>Advertiser must provide logo and artwork as press-quality JPG, EPS, TIF or PDF files</li>
    </ul>
  </section>

  <aside class="contact">
    <h4>AD QUESTIONS or ARTWORK:</h4>
    <p>LOTUS PATH MAGAZINE</p>
    <p>DANA MERCER</p>
    <p>PUBLISHER</p>
    <p>555-204-1187</p>
    <p>ads@lotuspathmag.example</p>
  </aside>
</main>
</body>
</html>
```